Home inspection business! professional look attracting customers just by looks. Read must haves

its a new business I started on my own for home inspections I would like something very professional to give to real estate agents and clients, its going to have my license number on it my business phone number my name my website as well etc on the back side it will be servicing areas and also what kind of services I offer I also have a business card from someone else the way I would like mine to be. I will attach my logo

Industry/Entity Type

Home Inspection

Contact Information for Business Card

listed in nice to haves

Requirements
Must have
• phone number - 718 352 9047
• website- crestwoodlatch.example
• license number #2749035186
• my name Gavin teraskovic
• picture of my logo and me on the front
• on the back of the card. stating I am servicing All of New York and Long Island
• also services I will offer will be home inspection -mold inspection -lead inspection -radon inspection -Termite Inspection -Infared Scan.
• and also we provide inspections for single family homes condos co-ops town-homes
• and commercial property
Nice to have
• same colors as the logos and also if you recommend fonts to look like the logo not sure up to you

```html
<!DOCTYPE html>
<html lang="en">
<head>
<meta charset="utf-8">
<title>Crestwood Latch Home Inspectors – Business Card</title>
<link href="https://fonts.googleapis.com/css2?family=Roboto:wght@400;500;700&family=Roboto+Condensed:wght@700&display=swap" rel="stylesheet">
<style>
  :root {
    --backdrop: #3a3a3c;
    --card: #1e1e20;
    --blue: #1b9ae4;
    --silver: #c9c9cb;
    --text: #d6d6d8;
  }
  * { box-sizing: border-box; margin: 0; padding: 0; }
  html, body { width: 799px; height: 1200px; overflow: hidden; }
  body {
    background: var(--backdrop);
    font-family: "Roboto", Arial, sans-serif;
    color: var(--text);
    position: relative;
  }
  .card {
    position: absolute;
    left: 60px;
    width: 680px;
    height: 390px;
    background: var(--card);
    border-radius: 6px;
    box-shadow: 0 10px 30px rgba(0,0,0,.45);
  }
  .card--front { top: 130px; }
  .card--back { top: 690px; }

  .brand { display: flex; align-items: center; gap: 12px; position: absolute; }
  .brand__dot { width: 30px; height: 30px; border-radius: 50%; background: var(--blue); flex: none; }
  .brand__name {
    font-weight: 500; color: var(--silver); line-height: 1.1;
    text-transform: uppercase; letter-spacing: 1px;
  }
  .card--front .brand { left: 50%; transform: translateX(-50%); top: 62px; }
  .card--front .brand__name { font-size: 30px; }
  .card--front .brand__sub { font-size: 17px; letter-spacing: 7px; display: block; }
  .card--back .brand { left: 40px; top: 46px; }
  .card--back .brand__name { font-size: 24px; }
  .card--back .brand__sub { font-size: 14px; letter-spacing: 6px; display: block; }

  .services-rule {
    position: absolute; left: 40px; right: 40px; top: 200px;
    height: 2px; background: var(--blue);
  }
  .services-tag {
    position: absolute; left: 50%; top: 186px; transform: translateX(-50%);
    background: var(--blue); color: #fff; font-weight: 700; font-size: 16px;
    padding: 6px 18px; border-radius: 16px; text-transform: uppercase;
  }
  .services-list {
    position: absolute; left: 30px; right: 30px; top: 240px;
    text-align: center; font-size: 18px; line-height: 1.55;
  }
  .sep { color: var(--blue); padding: 0 6px; }

  .person { position: absolute; left: 40px; top: 142px; }
  .person__name {
    font-family: "Roboto Condensed", Arial, sans-serif;
    color: var(--blue); font-size: 27px; font-weight: 700;
  }
  .person__role { font-size: 16px; margin-top: 2px; }
  .contacts { list-style: none; margin-top: 16px; }
  .contacts li { display: flex; align-items: center; gap: 10px; font-size: 16px; margin-bottom: 7px; }
  .contacts svg { width: 14px; height: 14px; fill: var(--blue); flex: none; }
  .accent { color: var(--blue); }

  .back-rule {
    position: absolute; left: 230px; right: 70px; top: 212px;
    height: 2px; background: var(--blue);
  }
  .back-mark {
    position: absolute; right: 50px; top: 196px;
    width: 24px; height: 24px; border-radius: 50%; border: 2px solid var(--silver);
  }
  .license {
    position: absolute; right: 48px; bottom: 48px;
    text-align: right; font-size: 18px; line-height: 1.35;
  }
</style>
</head>
<body>

<section class="card card--front" aria-label="Card back: services">
  <div class="brand">
    <span class="brand__dot"></span>
    <p class="brand__name">Crestwood Latch<span class="brand__sub">Home Inspectors</span></p>
  </div>
  <div class="services-rule"></div>
  <p class="services-tag">Our Services</p>
  <p class="services-list">
    Home Inspection<span class="sep">|</span>Mold Inspection<span class="sep">|</span>Lead Inspection<span class="sep">|</span>Radon Inspection<br>
    Termite Inspection<span class="sep">|</span>Infared Scan<span class="sep">|</span>Single Family Homes<br>
    Condos Co-ops Town<span class="sep">|</span>Homes &amp; Commercial Property
  </p>
</section>

<section class="card card--back" aria-label="Card front: contact">
  <div class="brand">
    <span class="brand__dot"></span>
    <p class="brand__name">Crestwood Latch<span class="brand__sub">Home Inspectors</span></p>
  </div>
  <div class="person">
    <h1 class="person__name">Gavin Teraskovic</h1>
    <p class="person__role">Managing Director</p>
    <ul class="contacts">
      <li><svg viewBox="0 0 24 24"><path d="M6.6 10.8a15.1 15.1 0 0 0 6.6 6.6l2.2-2.2a1 1 0 0 1 1-.25 11.4 11.4 0 0 0 3.6.57 1 1 0 0 1 1 1V20a1 1 0 0 1-1 1A17 17 0 0 1 3 4a1 1 0 0 1 1-1h3.5a1 1 0 0 1 1 1c0 1.25.2 2.45.57 3.57a1 1 0 0 1-.25 1z"/></svg>718 352 9047</li>
      <li><svg viewBox="0 0 24 24"><path d="M2 5h20v14H2z M2 5l10 8 10-8" stroke="#1e1e20" stroke-width="1.5"/></svg>gavin@crestwoodlatch.example</li>
      <li><svg viewBox="0 0 24 24"><circle cx="12" cy="12" r="10"/><path d="M2 12h20M12 2c3 3 3 17 0 20M12 2c-3 3-3 17 0 20" stroke="#1e1e20" stroke-width="1.5" fill="none"/></svg>www.<span class="accent">crestwoodlatch</span>.example</li>
    </ul>
  </div>
  <div class="back-rule"></div>
  <div class="back-mark"></div>
  <p class="license">License Number<br>#2749035186</p>
</section>

</body>
</html>
```